App for Lawyers & Accountants needs 'Professional' Styling

We want to style our app to convey a 'Professional' appearance. It's used by Lawyers, Accountants, Doctors etc. who take their work very seriously.

We currently trying to follow keystrel layout guidelines, but we find our app looks very bland. I've uploaded a screenshot of our current app, and two mock-ups of more stylized versions, but we're not happy with those mock-ups.

We'd like to see alternate designs for those two mock-ups, that look much more professional.

The specific elements we'd like to improve/focus on are:
* Colour of the top and left nav bars
* Appearance of the left nav, size, icons spacing
* Appearance of the buttons on the top right, so the user knows they are buttons they can press
* Spacing of the dashboard, background colour and spacing, colour/layout of the 'overdue' and 'todo' accordion headings in the 'my tasks' section.
* List view background grey, to be consistent with dashboard, but unobtrusive
* List view tabs to be obvious as tabs, but 'saved searches', filters and the export icon to still be associated with the data displayed, but it should be obvious to the user that those are different buttons, not just more tabs. (I.e. the filters button opens a panel below it that allows the user to filter the data in the list.)
* General appearance of the popup menu when you push the 'add' button on the top right

However, despite those specifics I'm sure it's all the subtle elements of the design that make a big difference.

Our brand colour is 1D4F91, and we use A20067 as a secondary colour in print media, (although it doesn't seem to work to well within the app.) Our brand font is signika. We'd like the designs to be based on those colours & font.

Target Market(s)

Professional people, Lawyers, Accountants, Doctors etc.

Font styles to use
Sans Serif
Other font styles liked:
• Signika

Colors
0255a3

Requirements
Must have
• The most 'Professional' experience/quality possible. Think the quality & brand image of vantrel desk, but taken to a higher level.
• An example/mock-up of the dashboard, list view and 'add' item popup menu
• Display the dashboard cards with the same information as our mock-ups - the information there is important and we don't have any extra cards to add (in the near term)
Nice to have
• Various colour combinations for the top and left nav bars, based on our primary blue brand colour, and perhaps some shade of dark grey.

```html
<!DOCTYPE html>
<html lang="en">
<head>
<meta charset="utf-8">
<title>AppName – Dashboard</title>
<link rel="stylesheet" href="https://fonts.googleapis.com/css2?family=Signika:wght@300;400;500;600&display=swap">
<style>
:root{
  --brand:#1D4F91;
  --accent:#A20067;
  --page:#f4f5f8;
  --card:#ffffff;
  --ink:#2b2f38;
  --muted:#8a8f9a;
  --faint:#b9bdc6;
  --line:#eceef2;
  --chart-fill:#d9dee8;
}
*{box-sizing:border-box;margin:0;padding:0}
html,body{width:1200px;height:920px;overflow:hidden}
body{font-family:"Signika",sans-serif;color:var(--ink);background:var(--page)}
.app{display:grid;grid-template-columns:200px 1fr;grid-template-rows:70px 1fr;width:1200px;height:920px}
.topbar{grid-column:1/3;display:flex;align-items:center;padding:0 28px;background:var(--page)}
.topbar .menu{width:20px;margin-right:18px}
.brand{display:flex;align-items:center;gap:10px;font-weight:600;font-size:17px;color:var(--brand);width:196px}
.brand .dot{width:30px;height:30px;border-radius:50%;background:var(--brand)}
.search{width:360px;height:34px;border-radius:4px;background:#eaecf1;display:flex;align-items:center;justify-content:space-between;padding:0 12px;font-size:13px;color:var(--muted);font-weight:300}
.top-actions{margin-left:auto;display:flex;align-items:center;gap:22px;font-size:14px}
.avatar{width:30px;height:30px;border-radius:50%;background:linear-gradient(135deg,#7a5a4a,#c9a58a)}
.user{display:flex;align-items:center;gap:10px}
.sidebar{position:relative;padding:20px 0 0 22px}
.add-btn{display:inline-flex;align-items:center;gap:12px;width:100px;height:34px;padding:0 14px;border-radius:17px;background:#fff;box-shadow:0 2px 6px rgba(0,0,0,.08);font-size:13px;color:var(--brand);font-weight:500;margin-bottom:26px}
.add-btn b{font-size:20px;font-weight:400}
.nav a{display:flex;align-items:center;gap:16px;height:42px;font-size:13px;color:#5d6270;text-decoration:none;position:relative;padding-left:6px}
.nav a.active{color:var(--brand);font-weight:500}
.nav a.active::before{content:"";position:absolute;left:-22px;top:10px;width:3px;height:22px;background:var(--brand)}
.nav svg{width:16px;height:16px}
.badge{margin-left:auto;margin-right:26px;width:18px;height:18px;border-radius:50%;background:var(--accent);color:#fff;font-size:10px;display:grid;place-items:center}
.settings{position:absolute;left:28px;bottom:30px;display:flex;gap:14px;align-items:center;font-size:13px;color:#5d6270}
.content{display:grid;grid-template-columns:300px 300px 1fr;gap:24px;padding:8px 28px 24px 10px;min-height:0}
.col{display:flex;flex-direction:column;min-height:0}
.col h2{font-size:17px;font-weight:400;margin:6px 0 14px 4px}
.card{background:var(--card);border-radius:6px;box-shadow:0 2px 10px rgba(30,40,70,.06)}
.tabs{display:flex;border-bottom:1px solid var(--line)}
.tabs span{flex:1;text-align:center;font-size:11px;padding:16px 0 12px;color:var(--muted);text-transform:uppercase;letter-spacing:.03em}
.tabs span.on{color:var(--accent);border-bottom:2px solid var(--accent)}
.task{display:grid;grid-template-columns:26px 1fr auto;padding:14px 18px 10px;column-gap:4px}
.task .chk{width:13px;height:13px;border:1.5px solid var(--faint);border-radius:50%;margin-top:2px}
.task .chk.done{background:var(--accent);border-color:var(--accent);display:grid;place-items:center}
.task .t{font-size:13px}
.task .d{font-size:11px;color:var(--faint);margin-top:4px}
.task .s{grid-column:2/4;font-size:11px;color:var(--muted);margin-top:4px;display:flex;gap:8px;align-items:center}
.mini{width:9px;height:7px;background:#7d8290;border-radius:1px;flex:none}
.time{padding:18px 16px 14px}
.stats{display:flex;justify-content:space-between;text-align:center}
.stat small{display:block;font-size:9px;text-transform:uppercase;color:var(--muted);letter-spacing:.04em;margin-bottom:6px}
.stat strong{font-size:19px;font-weight:400}
.stat.on small,.stat.on strong{color:var(--accent)}
.stat.on strong{border-bottom:2px solid var(--accent);padding-bottom:4px;display:inline-block}
.legend{display:flex;justify-content:space-around;font-size:11px;color:var(--muted);margin-top:8px}
.legend i{display:inline-block;width:9px;height:9px;border-radius:50%;margin-right:8px;vertical-align:-1px}
.docs{margin-top:0}
.doc{display:flex;align-items:center;gap:12px;padding:13px 18px;font-size:12px}
.doc .ic{width:13px;height:14px;border-radius:2px;background:var(--brand);flex:none}
.doc .ago{margin-left:auto;color:var(--faint);font-size:11px}
.matters{flex:1;overflow:hidden}
.matter{display:flex;gap:14px;padding:15px 18px;align-items:center}
.matter .ic{width:30px;height:30px;border-radius:50%;background:#f6eef3;display:grid;place-items:center;flex:none}
.matter .ic::after{content:"";width:12px;height:9px;border-radius:2px;background:var(--accent)}
.matter p{font-size:13px;line-height:1.3;flex:1}
.matter .ago{color:var(--faint);font-size:11px}
.row-div{height:1px;background:var(--line);margin:0 18px}
</style>
</head>
<body>
<div class="app">
  <header class="topbar">
    <svg class="menu" viewBox="0 0 20 14"><path d="M0 1h20M0 7h20M0 13h20" stroke="#555" stroke-width="1.6"/></svg>
    <div class="brand"><span class="dot"></span>AppName</div>
    <div class="search">Search everything
      <svg width="12" height="12" viewBox="0 0 12 12"><circle cx="5" cy="5" r="3.8" fill="none" stroke="#888" stroke-width="1.3"/><path d="M8 8l3 3" stroke="#888" stroke-width="1.3"/></svg>
    </div>
    <div class="top-actions">
      <svg width="18" height="18" viewBox="0 0 18 18"><circle cx="9" cy="9" r="7" fill="none" stroke="#555" stroke-width="1.5"/><path d="M9 5v4l3 2" stroke="#555" stroke-width="1.5" fill="none"/></svg>
      <svg width="18" height="18" viewBox="0 0 18 18"><path d="M9 2c-3 0-5 2-5 5v4l-2 3h14l-2-3V7c0-3-2-5-5-5z M7 15a2 2 0 0 0 4 0" fill="#555"/></svg>
      <div class="user"><span class="avatar" role="img" aria-label="User profile photo"></span>Dana R.
        <svg width="10" height="6" viewBox="0 0 10 6"><path d="M1 1l4 4 4-4" stroke="#555" fill="none" stroke-width="1.4"/></svg>
      </div>
    </div>
  </header>

  <aside class="sidebar">
    <div class="add-btn"><b>+</b>Add</div>
    <nav class="nav">
      <a class="active"><svg viewBox="0 0 16 16"><circle cx="8" cy="8" r="7" fill="var(--brand)"/><path d="M5 8.5l2 2 4-4" stroke="#fff" stroke-width="1.5" fill="none"/></svg>Dashboard</a>
      <a><svg viewBox="0 0 16 16"><rect x="1" y="4" width="14" height="10" rx="1" fill="#666"/><rect x="5" y="2" width="6" height="3" fill="none" stroke="#666"/></svg>My Matters</a>
      <a><svg viewBox="0 0 16 16"><circle cx="8" cy="5" r="3.5" fill="#666"/><path d="M1 15c0-4 3-6 7-6s7 2 7 6z" fill="#666"/></svg>Account</a>
      <a><svg viewBox="0 0 16 16"><path d="M3 1v14M3 2h10l-2 3 2 3H3" fill="#666" stroke="#666"/></svg>My Tasks<span class="badge">24</span></a>
      <a><svg viewBox="0 0 16 16"><path d="M11 5L6 10a1.5 1.5 0 0 0 2 2l6-6a3 3 0 0 0-4-4L4 8a4.5 4.5 0 0 0 6 6l4-4" fill="none" stroke="#666" stroke-width="1.3"/></svg>Documents</a>
      <a><svg viewBox="0 0 16 16"><circle cx="8" cy="8" r="6.5" fill="none" stroke="#666" stroke-width="1.4"/><path d="M8 4v4l3 2" stroke="#666" stroke-width="1.4" fill="none"/></svg>Time Records</a>
    </nav>
    <div class="settings"><svg width="16" height="16" viewBox="0 0 16 16"><circle cx="8" cy="8" r="5" fill="none" stroke="#555" stroke-width="3" stroke-dasharray="2.5 1.4"/><circle cx="8" cy="8" r="2" fill="#555"/></svg>Settings</div>
  </aside>

  <main class="content">
    <section class="col">
      <h2>My Tasks</h2>
      <div class="card">
        <div class="tabs"><span>Overdue (4)</span><span class="on">To Do (20)</span></div>
        <div class="task"><span class="chk done"><svg width="7" height="6" viewBox="0 0 7 6"><path d="M1 3l2 2 3-4" stroke="#fff" fill="none" stroke-width="1.3"/></svg></span><span class="t">Finalise Court Documents</span><span class="d">Today</span><span class="s"><i class="mini"></i>1157 Vance v. The State of...</span></div>
        <div class="task"><span class="chk"></span><span class="t">Task #2</span><span class="d">Tomorrow</span><span class="s"><i class="mini"></i>Owen Brisk</span></div>
        <div class="task"><span class="chk"></span><span class="t">Finalise Court Settlement Figures</span><span class="d">15 May 2018</span><span class="s"><i class="mini"></i>1302 Delmar Holdings v. The State of...</span></div>
        <div class="task"><span class="chk"></span><span class="t">This is my 4th task</span><span class="d">18 May 2018</span><span class="s"><i class="mini"></i>Short meeting with Mara Quill</span></div>
        <div class="task"><span class="chk"></span><span class="t">No. 5 task</span><span class="d">22 May 2018</span><span class="s"><i class="mini"></i>Report to Harbor HQ</span></div>
        <div class="task"><span class="chk"></span><span class="t">Finalise Court Documents</span><span class="d">26 May 2018</span><span class="s"><i class="mini"></i>1157 Vance v. The State of...</span></div>
        <div class="task"><span class="chk"></span><span class="t">Task #7</span><span class="d">27 May 2018</span><span class="s"><i class="mini"></i>Owen Brisk</span></div>
        <div class="task"><span class="chk"></span><span class="t">Finalise Court Settlement Figures</span><span class="d">1 Jun 2018</span><span class="s"><i class="mini"></i>1302 Delmar Holdings v. The State of...</span></div>
        <div class="task"><span class="chk"></span><span class="t">This is my 9th task</span><span class="d">16 Jun 2018</span><span class="s"><i class="mini"></i>Short meeting with Mara Quill</span></div>
        <div class="task"><span class="chk"></span><span class="t">No. 10 task</span><span class="d">4 Jul 2018</span><span class="s"><i class="mini"></i>Report to Harbor HQ</span></div>
      </div>
    </section>

    <section class="col">
      <h2>My Time Records</h2>
      <div class="card time">
        <div class="stats">
          <div class="stat"><small>Today</small><strong>5h 2m</strong></div>
          <div class="stat on"><small>This Week</small><strong>24h 7m</strong></div>
          <div class="stat"><small>This Month</small><strong>56h 34m</strong></div>
        </div>
        <svg width="268" height="140" viewBox="0 0 268 140" style="margin-top:12px">
          <g font-family="Signika,sans-serif" font-size="8" fill="#8a8f9a">
            <text x="0" y="12">10h</text><text x="0" y="34">8h</text><text x="0" y="56">6h</text><text x="0" y="78">4h</text><text x="0" y="100">2h</text>
          </g>
          <path d="M0 70 C40 70 60 118 120 100 S190 60 268 85 V114 H0Z" fill="var(--chart-fill)"/>
          <path d="M0 112 C30 112 45 88 75 78 S120 112 150 100 S190 60 215 68 S245 72 268 64" fill="none" stroke="var(--accent)" stroke-width="2"/>
          <circle cx="210" cy="67" r="4.5" fill="#fff" stroke="var(--accent)" stroke-width="2"/>
          <g font-family="Signika,sans-serif" font-size="7" fill="#8a8f9a" text-anchor="middle">
            <text x="30" y="124">S</text><text x="60" y="124">M</text><text x="90" y="124">T</text><text x="120" y="124">W</text><text x="150" y="124">T</text><text x="180" y="124">F</text><text x="210" y="124">S</text>
            <text x="30" y="136">6</text><text x="60" y="136">7</text><text x="90" y="136">8</text><text x="120" y="136">9</text><text x="150" y="136">10</text><text x="180" y="136">11</text><text x="210" y="136">12</text>
          </g>
        </svg>
        <div class="legend"><span><i style="background:#b8c1d4"></i>Last Week</span><span><i style="background:var(--accent)"></i>Last Week</span></div>
      </div>

      <h2 style="margin-top:26px">My Recent Documents</h2>
      <div class="card docs">
        <div class="doc"><i class="ic"></i>Court Doc101<span class="ago">1h</span></div>
        <div class="doc"><i class="ic"></i>Settlement Figures_Rk-Moreno<span class="ago">4h</span></div>
        <div class="doc"><i class="ic"></i>Harbor 2018 Presentation<span class="ago">9h</span></div>
        <div class="doc"><i class="ic"></i>For Task XYZ000<span class="ago">12h</span></div>
        <div class="doc"><i class="ic"></i>Settlement Figures_Mara-Quill<span class="ago">1d</span></div>
      </div>
    </section>

    <section class="col">
      <h2>My Recent Matters</h2>
      <div class="card matters">
        <div class="matter"><span class="ic"></span><p>1157 Alder v. Director of Public Persecutions concerning motor vehicle</p><span class="ago">2h</span></div><div class="row-div"></div>
        <div class="matter"><span class="ic"></span><p>The generated Lorem Ipsum is there-fore always free from repetition</p><span class="ago">5h</span></div><div class="row-div"></div>
        <div class="matter"><span class="ic"></span><p>1024 Lorem Ipsum is not simply random text.</p><span class="ago">12h</span></div><div class="row-div"></div>
        <div class="matter"><span class="ic"></span><p>Elias Warner, a Latin professor at Linden Hall College in Virginia</p><span class="ago">20h</span></div><div class="row-div"></div>
        <div class="matter"><span class="ic"></span><p>The standard chunk of Lorem Ipsum used since the 1500s</p><span class="ago">1d</span></div><div class="row-div"></div>
        <div class="matter"><span class="ic"></span><p>1157 Alder v. Director of Public Persecutions concerning motor vehicle</p><span class="ago">2d</span></div><div class="row-div"></div>
        <div class="matter"><span class="ic"></span><p>The generated Lorem Ipsum is there-fore always free from repetition</p><span class="ago">5d</span></div><div class="row-div"></div>
        <div class="matter"><span class="ic"></span><p>1024 Lorem Ipsum is not simply random text.</p><span class="ago">7d</span></div><div class="row-div"></div>
        <div class="matter"><span class="ic"></span><p>Elias Warner, a Latin professor at Linden Hall College in Virginia</p><span class="ago">1w</span></div><div class="row-div"></div>
        <div class="matter"><span class="ic"></span><p>The standard chunk of Lorem Ipsum used since the 1500s</p><span class="ago">1w</span></div>
      </div>
    </section>
  </main>
</div>
</body>
</html>
```